Family Values Poster

We are a mixed Indian Caucasian family of 3 (soon to be 4). We want to hang up a well designed poster of our values as a family. I have seen some designs with a little visual icon representing each value which I liked. Poster needs to have all the values listed and printer friendly graphics.
Thanks! - Maren

Our Family Values

We value:

Creative Activities
Global Community Exploration
Fitness and Healthful Eating
Adventure
Personal Cleanliness
Rest
Kindness to Self and Others
Open Communication
Gratitude
Taking Responsibility
Investing Wisely (time, money, people)

```html
<!DOCTYPE html>
<html lang="en">
<head>
<meta charset="UTF-8">
<title>Our Family Values</title>
<link rel="stylesheet" href="https://fonts.googleapis.com/css2?family=Satisfy&family=Raleway:wght@600;700&display=swap">
<style>
  :root {
    --backdrop: #f7f3ab;
    --sun: #f5ed6c;
    --sun-pale: #f7f2a9;
    --night: #231b2d;
    --ink: #0b0b0b;
    --photo-light: #5a5a5a;
    --photo-dark: #111111;
    --white: #ffffff;
  }
  * { margin: 0; padding: 0; box-sizing: border-box; }
  html, body {
    width: 1200px;
    height: 1200px;
    overflow: hidden;
    background: var(--backdrop);
  }
  .poster {
    position: absolute;
    left: 213px;
    top: 20px;
    width: 774px;
    height: 1160px;
    background: var(--ink);
    overflow: hidden;
  }
  .hero-photo {
    position: absolute;
    left: 0;
    top: 200px;
    width: 774px;
    height: 487px;
    background: radial-gradient(ellipse at 55% 35%, var(--photo-light) 0%, #2c2c2c 40%, var(--photo-dark) 75%);
  }
  .header-shapes {
    position: absolute;
    left: 0;
    top: 0;
    width: 774px;
    height: 320px;
  }
  .title {
    position: absolute;
    left: 0;
    right: 0;
    top: 62px;
    padding-left: 60px;
    text-align: center;
    font-family: "Satisfy", cursive;
    font-size: 66px;
    letter-spacing: 0.09em;
    color: var(--ink);
    line-height: 1;
  }
  .feet-triangle {
    position: absolute;
    left: 0;
    top: 0;
    width: 774px;
    height: 687px;
  }
  .we-value {
    position: absolute;
    right: 27px;
    top: 590px;
    font-family: "Satisfy", cursive;
    font-size: 54px;
    letter-spacing: 0.06em;
    color: var(--sun);
    line-height: 1;
  }
  .values-panel {
    position: absolute;
    left: 0;
    top: 687px;
    width: 774px;
    height: 450px;
    background: var(--night);
    overflow: hidden;
  }
  .footer-band {
    position: absolute;
    left: 0;
    top: 1137px;
    width: 774px;
    height: 23px;
    background: var(--sun);
  }
  .rings {
    position: absolute;
    left: 0;
    top: 0;
    width: 774px;
    height: 450px;
  }
  .value-list {
    position: absolute;
    list-style: none;
    font-family: "Raleway", sans-serif;
    font-weight: 700;
    font-size: 19.5px;
    letter-spacing: 0.14em;
    line-height: 26.7px;
    text-transform: uppercase;
  }
  .value-list--lifestyle {
    right: 27px;
    top: 28px;
    text-align: right;
    color: var(--white);
  }
  .value-list--character {
    left: 24px;
    top: 232px;
    text-align: left;
    color: var(--sun);
  }
</style>
</head>
<body>
  <main class="poster">
    <div class="hero-photo" role="img" aria-label="Black and white photo of family hands linked together, adult and child wrists clasped"></div>

    <svg class="header-shapes" viewBox="0 0 774 320" aria-hidden="true">
      <polygon points="0,0 774,0 774,300 0,233" fill="var(--sun-pale)"/>
      <polygon points="0,0 774,0 774,272 0,173" fill="var(--sun)"/>
    </svg>

    <h1 class="title">Our Family Values</h1>

    <svg class="feet-triangle" viewBox="0 0 774 687">
      <polygon points="18,600 85,480 150,600" fill="#9a9a9a" role="img" aria-label="Photo of a baby's feet in a triangle frame"/>
      <polygon points="48,609 134,463 234,609" fill="var(--sun)" fill-opacity="0.8" role="img" aria-label="Yellow triangle overlay on a photo of a baby's feet"/>
    </svg>

    <p class="we-value">We value</p>

    <section class="values-panel">
      <svg class="rings" viewBox="0 0 774 450" aria-hidden="true">
        <g fill="none" stroke="var(--sun)" stroke-width="6">
          <circle cx="0" cy="110" r="58"/>
          <circle cx="0" cy="110" r="74"/>
          <circle cx="774" cy="313" r="58"/>
          <circle cx="774" cy="313" r="74"/>
        </g>
        <circle cx="0" cy="110" r="42" fill="var(--sun)"/>
        <circle cx="774" cy="313" r="42" fill="var(--sun)"/>
      </svg>

      <ul class="value-list value-list--lifestyle">
        <li>Creative Activities</li>
        <li>Global Community Exploration</li>
        <li>Fitness and Healthful Eating</li>
        <li>Adventure</li>
        <li>Personal Cleanliness</li>
        <li>Rest</li>
      </ul>

      <ul class="value-list value-list--character">
        <li>Kindness to Self and Others</li>
        <li>Open Communication</li>
        <li>Gratitude</li>
        <li>Taking Responsibility</li>
        <li>Investing Wisely</li>
      </ul>
    </section>

    <div class="footer-band"></div>
  </main>
</body>
</html>
```